Pivots & Treads .com

This website is simple!!!
Landing page background image should capture the customers attention!!! We will provide a image as a example of what we like. The purpose for this website is to provide customers with a clean easy way to request a quote for industrial casters and wheels by OEM’s as well as maintenance departments worldwide. Please see if you can follow our thought process below.
Customer comes to website, they are invited to Request a Quote by providing us with Manufacturer Name, Manufacturers Part # and quantity needed.
If this is not known the customer will complete will WP conversation format form answering about 10 questions
Or
Look up the part number in one of the 8 to 12 catalogs located in the Flippin Book format on our catalog page, or equal plug in .
When the client request a quote a account page will pop up request The following:
Clients first and last name
Email address
And optional questions
Company name and best contact number.
Once this is complete customer will hit SUBMIT.
The customers request will be in system. A email will be sent to Customer service notifying us the Quote Request has been made.
We will then build a quote for the customer with a good, better and best options. Customers Request a Quote submission may have more than one caster or wheel requested at a time, so website must allow this.
When the customer comes back into website there email address will come up as the account name and request a password be made for them. This will allow them to store quotes in their account for future needs. If quote is older than 30 day the system will trigger a button at the bottom of the quote for resubmit Request for updated quote.
Once customer reviews quote the quote can be Converted to order within the website.
Once Converted the system will send us a email and order will be processed.
We will need a Chat program that will text to CS the questions.
You will need to have high quality graphic design skills on your team.
We have found 2 plugins that would work nicely with our new website Flippin books to showcase our catalogs for customers to research and WPForms conversation forms to complete request for quote form.
Just Ideas:
Very very ghosted caster blueprint in white background but very very ghosted or the icon just idea
We have never had a font used we like
Grayscale every except for rubber on wheels and logo icon
Website should have hamburger menu on left
Website should hav responsive deign
Account head on right side
Has anyone read the brief from top to bottom and the updates, I’m seeing a lot of duplicates of the website I posted in images I want a clean website With lite backgrand with the poly being definite colors on each wheel I added a green yellow and red image has anyone looked at that Just a question?
Went on vacation/holiday

```html
<!DOCTYPE html>
<html lang="en">
<head>
<meta charset="utf-8">
<title>Pivots &amp; Treads .com</title>
<link href="https://fonts.googleapis.com/css2?family=Montserrat:wght@400;500;600;700;800&family=Raleway:wght@400;500;600&display=swap" rel="stylesheet">
<style>
:root{
  --ink:#2b2b2b;
  --dark:#333333;
  --brand:#24479b;
  --light:#ececec;
  --panel:#e6e6e6;
  --white:#ffffff;
  --muted:#555555;
}
*{box-sizing:border-box;margin:0;padding:0}
html,body{width:1200px;height:2711px;overflow:hidden}
body{position:relative;background:var(--white);font-family:"Montserrat",sans-serif;color:var(--ink)}
.abs{position:absolute}
.topbar{left:0;top:0;width:1200px;height:30px;background:var(--ink)}
.topbar .social{left:150px;top:7px;display:flex;gap:6px}
.dot{width:17px;height:17px;border-radius:50%;background:#bdbdbd;display:block}
.topbar .phone{right:152px;top:7px;color:#fff;font-size:11px;font-weight:600;display:flex;align-items:center;gap:8px}
.topbar .phone .acc{width:17px;height:17px;border-radius:50%;background:#e0e0e0;margin-left:16px}
.header{left:0;top:30px;width:1200px;height:77px;background:var(--light);border-bottom:1px solid #d4d4d4}
.logo{display:flex;align-items:center;gap:10px;color:var(--brand);font-weight:800;letter-spacing:1px;line-height:1}
.logo .mark{border-radius:50%;background:var(--brand);flex:none}
.logo .name{display:flex;flex-direction:column}
.header .logo{left:150px;top:12px;font-size:26px}
.header .logo .mark{width:50px;height:50px}
.nav{left:502px;top:0;height:77px;display:flex;gap:0;font-size:13px;font-weight:600;color:#444}
.nav a{display:block;height:77px;line-height:68px;padding:0 8px;color:inherit;text-decoration:none;margin-right:23px}
.nav a.active{border-bottom:3px solid var(--brand)}
.btn-quote{left:887px;top:16px;width:163px;height:45px;background:var(--brand);color:#fff;font-size:13px;font-weight:600;display:flex;align-items:center;justify-content:center}
.hero{left:0;top:107px;width:1200px;height:450px;background:linear-gradient(90deg,#d7d2c9 0%,#c9c3b8 45%,#b8b3ab 100%)}
.hero-img{left:520px;top:190px;width:540px;height:320px;border-radius:8px;background:radial-gradient(circle at 15% 60%,#d8393a 0,#d8393a 12%,transparent 13%),radial-gradient(circle at 50% 60%,#2e3b63 0,#2e3b63 12%,transparent 13%),radial-gradient(circle at 85% 55%,#8f9499 0,#8f9499 13%,transparent 14%)}
.hero h1{left:150px;top:195px;width:500px;font-size:29px;line-height:42px;font-weight:600;color:var(--brand)}
.hero ul{left:152px;top:295px;list-style:none;font-size:19px;font-weight:500;letter-spacing:.6px;color:#333}
.hero li{display:flex;align-items:center;gap:16px;height:36px}
.ico{width:19px;height:19px;flex:none}
.btn-dark{background:var(--ink);color:#fff;font-weight:600;display:flex;align-items:center;justify-content:center}
.hero .learn{left:189px;top:418px;width:150px;height:45px;font-size:18px}
.band{left:0;background:var(--ink);color:#fff;font-weight:600;display:flex;align-items:center}
.band-solutions{top:660px;width:573px;height:57px;font-size:20px;padding-left:150px;letter-spacing:.8px}
.easy{left:150px;top:780px;font-size:22px;font-weight:500;letter-spacing:1px}
.steps{left:150px;top:862px;list-style:none;font-size:18px;font-weight:500;letter-spacing:.8px}
.steps li{display:flex;align-items:center;gap:16px;height:36px}
.quote-card{left:659px;top:614px;width:392px;height:484px;background:var(--panel);box-shadow:0 2px 4px rgba(0,0,0,.2)}
.label{font-size:13px;font-weight:600;letter-spacing:.5px;color:#333}
.select{background:#fff;border:2px solid #b9c3dc;height:37px;display:flex;align-items:center;justify-content:space-between;padding:0 14px;font-size:13px;font-weight:600;letter-spacing:.5px;color:#333}
.btn-get{left:704px;top:959px;width:300px;height:45px;background:var(--brand);color:#fff;font-size:13px;font-weight:600;letter-spacing:.8px;display:flex;align-items:center;justify-content:center}
.no-details{left:704px;top:1039px;font-size:13px;font-weight:500;color:#333}
.no-details span{color:var(--brand)}
.products{left:0;top:1154px;width:1200px;height:584px;background:#ebebeb}
.products h2{left:173px;top:1222px;font-size:24px;font-weight:600;letter-spacing:1.5px;color:#333}
.view-all{left:893px;top:1209px;width:157px;height:52px;font-size:18px;gap:10px}
.card{top:1316px;width:263px;height:262px;background:#fff;box-shadow:0 1px 3px rgba(0,0,0,.15)}
.card .photo{position:absolute;left:40px;top:30px;width:183px;height:200px;border-radius:8px}
.card-title{top:1589px;width:263px;text-align:center;font-size:19px;font-weight:500;letter-spacing:.5px;color:#333}
.card-btn{top:1638px;width:134px;height:44px;font-size:16px}
.band-about{top:1795px;width:348px;height:57px;font-size:21px;justify-content:center;letter-spacing:1px}
.about-logo{left:776px;top:1793px;font-size:27px}
.about-logo .mark{width:52px;height:52px}
.about-text{left:214px;top:1898px;width:374px;height:422px;background:#ececec;box-shadow:0 1px 4px rgba(0,0,0,.2);padding:36px 36px 0 40px;font-family:"Raleway",sans-serif;font-size:14.5px;line-height:21px;color:#333}
.about-text p{margin-bottom:19px}
.about-img{left:716px;top:1937px;width:368px;height:389px;background:radial-gradient(circle at 40% 62%,#e3b52c 0,#e3b52c 28%,#fafafa 30%)}
.footer{left:0;top:2376px;width:1200px;height:308px;background:#e9e9e9}
.f-head{top:2430px;font-size:15px;font-weight:500;color:#333;line-height:18px;text-transform:uppercase}
.f-head b{font-weight:500}
.f-rule{top:2456px;height:2px;background:linear-gradient(90deg,var(--brand) 0 80px,#cfd6e6 80px)}
.footer-logo{left:150px;top:2486px;font-size:19px}
.footer-logo .mark{width:40px;height:40px}
.f-copy{left:150px;top:2555px;width:240px;font-family:"Raleway",sans-serif;font-size:11px;line-height:19px;color:#444}
.contact{left:483px;font-family:"Raleway",sans-serif;font-size:12.5px;line-height:19px;color:#333;display:flex;gap:20px;align-items:flex-start}
.contact svg{width:14px;height:14px;margin-top:3px;flex:none}
.subscribe{left:783px;top:2499px;width:267px;height:29px;display:flex}
.subscribe .input{flex:1;background:#fff;border:1px solid #b9c3dc;font-family:"Raleway",sans-serif;font-size:11px;color:#666;padding-left:16px;display:flex;align-items:center}
.subscribe .go{width:91px;background:var(--brand);color:#fff;font-size:11.5px;font-weight:600;display:flex;align-items:center;justify-content:center}
.f-social{left:783px;top:2566px;display:flex;gap:14px}
.f-social .dot{width:23px;height:23px;background:#555}
.bottombar{left:0;top:2684px;width:1200px;height:27px;background:var(--ink);color:#fff;font-size:8.5px;font-weight:500;display:flex;align-items:center;justify-content:center;gap:10px}
</style>
</head>
<body>

<div class="abs topbar">
  <div class="abs social"><span class="dot"></span><span class="dot"></span><span class="dot"></span><span class="dot"></span><span class="dot"></span></div>
  <div class="abs phone">
    <svg class="ico" viewBox="0 0 20 20" style="width:14px;height:14px"><path fill="#fff" d="M4 2l3 0 1.5 4-2 1.5a10 10 0 0 0 6 6l1.5-2 4 1.5v3a2 2 0 0 1-2 2A16 16 0 0 1 2 4a2 2 0 0 1 2-2z"/></svg>
    0140 555 0192<span class="acc"></span>
  </div>
</div>

<header class="abs header">
  <div class="abs logo"><span class="mark"></span><span class="name"><span>PIVOTS &amp;</span><span>TREADS .com</span></span></div>
  <nav class="abs nav">
    <a href="#">Home</a><a href="#">Products</a><a href="#" class="active">About Us</a><a href="#">Contact Us</a>
  </nav>
  <div class="abs btn-quote">REQUEST A QUOTE</div>
</header>

<section class="abs hero" role="img" aria-label="Blurred warehouse interior photograph"></section>
<div class="abs hero-img" role="img" aria-label="Red caster, navy caster and grey wheel product photos"></div>
<div class="hero">
  <h1 class="abs">One Stop Solution for All Your Caster Wheel Applications</h1>
  <ul class="abs">
    <li><svg class="ico" viewBox="0 0 20 20"><circle cx="10" cy="10" r="10" fill="#24479b"/><path fill="#fff" d="M10 4l1.8 3.8 4 .4-3 2.7.9 4-3.7-2.1-3.7 2.1.9-4-3-2.7 4-.4z"/></svg>High Quality Caster Wheels</li>
    <li><svg class="ico" viewBox="0 0 20 20"><circle cx="10" cy="10" r="10" fill="#24479b"/><path fill="#fff" d="M10 4l1.8 3.8 4 .4-3 2.7.9 4-3.7-2.1-3.7 2.1.9-4-3-2.7 4-.4z"/></svg>Huge Product Range</li>
    <li><svg class="ico" viewBox="0 0 20 20"><circle cx="10" cy="10" r="10" fill="#24479b"/><path fill="#fff" d="M10 4l1.8 3.8 4 .4-3 2.7.9 4-3.7-2.1-3.7 2.1.9-4-3-2.7 4-.4z"/></svg>Reasonable Price</li>
  </ul>
  <div class="abs btn-dark learn">Learn More</div>
</div>

<div class="abs band band-solutions">Solutions for All Your Applications</div>
<div class="abs easy">Easy as 1-2-3</div>
<ul class="abs steps">
  <li><svg class="ico" viewBox="0 0 20 20"><circle cx="10" cy="10" r="10" fill="#24479b"/><path d="M8 5.5l4.5 4.5L8 14.5" fill="none" stroke="#fff" stroke-width="2.2"/></svg>Request a Quote</li>
  <li><svg class="ico" viewBox="0 0 20 20"><circle cx="10" cy="10" r="10" fill="#24479b"/><path d="M8 5.5l4.5 4.5L8 14.5" fill="none" stroke="#fff" stroke-width="2.2"/></svg>Receive a Quote</li>
  <li><svg class="ico" viewBox="0 0 20 20"><circle cx="10" cy="10" r="10" fill="#24479b"/><path d="M8 5.5l4.5 4.5L8 14.5" fill="none" stroke="#fff" stroke-width="2.2"/></svg>Convert a Quote to Order</li>
</ul>

<div class="abs quote-card"></div>
<div class="abs label" style="left:704px;top:657px">Manufacturer’s Name:</div>
<div class="abs select" style="left:704px;top:685px;width:300px">Select<svg width="16" height="10" viewBox="0 0 16 10"><path d="M1 1l7 7 7-7" fill="none" stroke="#222" stroke-width="2.4"/></svg></div>
<div class="abs label" style="left:704px;top:766px">Manufacturer’s Part Number:</div>
<div class="abs select" style="left:704px;top:795px;width:300px">Select<svg width="16" height="10" viewBox="0 0 16 10"><path d="M1 1l7 7 7-7" fill="none" stroke="#222" stroke-width="2.4"/></svg></div>
<div class="abs label" style="left:704px;top:887px">Quantity:</div>
<div class="abs select" style="left:855px;top:877px;width:149px;font-size:11px">1<svg width="16" height="10" viewBox="0 0 16 10"><path d="M1 1l7 7 7-7" fill="none" stroke="#222" stroke-width="2.4"/></svg></div>
<div class="abs btn-get">GET QUOTE</div>
<div class="abs no-details">Don’t Have Manufacturer Details? <span>Click Here</span></div>

<section class="abs products"></section>
<h2 class="abs" style="left:173px;top:1222px;font-size:24px;font-weight:600;letter-spacing:1.5px;color:#333">Our Products</h2>
<div class="abs btn-dark view-all">View All <svg width="9" height="14" viewBox="0 0 9 14"><path d="M1.5 1.5L7 7l-5.5 5.5" fill="none" stroke="#fff" stroke-width="2"/></svg></div>

<div class="abs card" style="left:150px"><div class="photo" role="img" aria-label="Red swivel caster product photo" style="background:radial-gradient(circle at 45% 60%,#d8393a 0,#d8393a 35%,#fff 37%)"></div></div>
<div class="abs card" style="left:468px"><div class="photo" role="img" aria-label="Navy swivel caster product photo" style="background:radial-gradient(circle at 45% 60%,#2e3b63 0,#2e3b63 35%,#fff 37%)"></div></div>
<div class="abs card" style="left:787px"><div class="photo" role="img" aria-label="Grey wheel with black hub product photo" style="background:radial-gradient(circle at 50% 50%,#2a2a2a 0,#2a2a2a 22%,#9a9ea3 23%,#9a9ea3 38%,#fff 40%)"></div></div>
<div class="abs card-title" style="left:150px">Casters</div>
<div class="abs card-title" style="left:468px">Casters</div>
<div class="abs card-title" style="left:787px">Wheels</div>
<div class="abs btn-dark card-btn" style="left:214px">Learn More</div>
<div class="abs btn-dark card-btn" style="left:533px">Learn More</div>
<div class="abs btn-dark card-btn" style="left:852px">Learn More</div>

<div class="abs band band-about">About Us</div>
<div class="abs logo about-logo"><span class="mark"></span><span class="name"><span>PIVOTS &amp;</span><span>TREADS .com</span></span></div>
<div class="abs about-text">
  <p>Lorem ipsum dolor sit amet, consectetur adipiscing elit, sed do eiusmod tempor incididunt ut labore et dolore magna aliqua Quis ipsum suspendisse ultrices gravida. Risus commodo</p>
  <p>Lorem ipsum dolor sit amet, consectetur adipiscing elit, sed do eiusmod tempor incididunt ut labore et dolore magna aliqua Quis ipsum suspendisse ultrices gravida.</p>
  <p>Lorem ipsum dolor sit amet, consectetur adipiscing elit, sed do eiusmod tempor incididunt ut labore et dolore magna aliqua Quis ipsum suspendisse ultrices gravida. Lorem ipsum dolor sit amet, consectetur adipiscing elit, sed do eiusmod tempor</p>
</div>
<div class="abs about-img" role="img" aria-label="Yellow polyurethane swivel caster with brake, product photo"></div>

<footer class="abs footer"></footer>
<div class="abs f-head" style="left:150px">About <b>Us</b></div>
<div class="abs f-rule" style="left:150px;width:276px"></div>
<div class="abs f-head" style="left:483px">Contact <b>Us</b></div>
<div class="abs f-rule" style="left:483px;width:243px"></div>
<div class="abs f-head" style="left:782px">Subscribe to our<br>newsletter</div>
<div class="abs logo footer-logo"><span class="mark"></span><span class="name"><span>PIVOTS &amp;</span><span>TREADS .com</span></span></div>
<div class="abs f-copy">Lorem ipsum dolor sit amet, consectetur adipiscing elit, sed do eiusmod tempor incididunt ut labore et dolore magna aliqua. Quis ipsum suspendisse ultrices gravida.</div>
<div class="abs contact" style="top:2486px"><svg viewBox="0 0 14 14"><path fill="#333" d="M7 0a5 5 0 0 1 5 5c0 4-5 9-5 9S2 9 2 5a5 5 0 0 1 5-5zm0 3a2 2 0 1 0 0 4 2 2 0 0 0 0-4z"/></svg><span>18 Foundry Lane, Millbrook,<br>Ohio, 44012</span></div>
<div class="abs contact" style="top:2552px"><svg viewBox="0 0 14 14"><path fill="#333" d="M0 3h14v9H0z"/><path d="M0 3l7 5 7-5" fill="none" stroke="#e9e9e9" stroke-width="1.2"/></svg><span>hello@pivotstreads.com</span></div>
<div class="abs contact" style="top:2605px"><svg viewBox="0 0 20 20"><path fill="#333" d="M4 2l3 0 1.5 4-2 1.5a10 10 0 0 0 6 6l1.5-2 4 1.5v3a2 2 0 0 1-2 2A16 16 0 0 1 2 4a2 2 0 0 1 2-2z"/></svg><span>0140 555 0192</span></div>
<div class="abs subscribe"><div class="input">Enter Your Email</div><div class="go">Subscribe</div></div>
<div class="abs f-social"><span class="dot"></span><span class="dot"></span><span class="dot"></span><span class="dot"></span><span class="dot"></span></div>

<div class="abs bottombar"><span>Copyright © 2022 Pivots and Treads.com</span><span>|</span><span>Terms of Service</span><span>|</span><span>Privacy Policy</span></div>

</body>
</html>
```